Consultancy Business Card Design

We need a business card design for a new company based in singapore called FortyOne. FortyOne a boutique consultancy firm offering broad-based business solutions, from conception to re-invention, for ventures from new start-ups to long-running traditional businesses.
Its 2 main divisions (Food & Beverage Operations and Construction & Project Management) have access to a wide range of networks, knowledge bases, and resources to service its clients across numerous diverse sectors. This includes, and is not limited to, construction, F&B, and retail.
We are a company that combines the ambition, boldness and energy of one in the 20s with the dedication, level-headedness and dependability of one entering its 30s. Bridging the experiences of the old with ideals of the young, we draw on the positives of both to create a unique synergy.
We hope to see designs that fits our company profile.
Boutique
FortyOne(Company Name)
Marcus Leow (Name)
Principle Consultant (Title)
F&B and Hospitality (Division)
(+65) 8364 5170 (Contact no.)
marcus@fortyone-example.com.sg (Email)

```html
<!DOCTYPE html>
<html lang="en">
<head>
<meta charset="utf-8">
<title>FortyOne Business Card</title>
<link rel="stylesheet" href="https://fonts.googleapis.com/css2?family=Saira+Extra+Condensed:wght@400;600&family=Saira:ital,wght@1,200&display=swap">
<style>
  :root {
    --canvas: #ffffff;
    --card-light: #222222;
    --card-dark: #131313;
    --accent: #ffd400;
    --watermark: rgba(255, 212, 0, 0.05);
    --icon-ink: #121212;
  }
  * { box-sizing: border-box; margin: 0; padding: 0; }
  html, body {
    width: 1200px; height: 1000px; overflow: hidden;
    background: var(--canvas);
  }
  .canvas { position: relative; width: 1200px; height: 1000px; }
  .card {
    position: absolute; overflow: hidden; display: block;
    background: radial-gradient(ellipse at 50% 45%, var(--card-light) 0%, var(--card-dark) 75%);
  }
  .card--front { left: 20px; top: 22px; width: 765px; height: 437px; }
  .card--back { left: 385px; top: 479px; width: 795px; height: 454px; }

  .condensed { font-family: "Saira Extra Condensed", "Arial Narrow", sans-serif; }
  .wordmark { font-weight: 600; fill: var(--accent); }
  .watermark { font-weight: 600; fill: var(--watermark); }
  .person-name {
    font-family: "Saira", sans-serif; font-style: italic; font-weight: 200;
    fill: var(--accent);
  }
  .detail { font-weight: 400; fill: var(--accent); }
  .name-rule { stroke: var(--accent); stroke-width: 2; }
  .icon-disc { fill: var(--accent); }
  .icon-ink { fill: var(--icon-ink); }
  .icon-line { fill: none; stroke: var(--icon-ink); stroke-width: 2.5; }
</style>
</head>
<body>
<div class="canvas">
  <svg class="card card--front" viewBox="0 0 765 437" role="group" aria-label="Card front">
    <text class="condensed wordmark" x="175" y="283" font-size="250" textLength="420" lengthAdjust="spacingAndGlyphs">fortyone</text>
  </svg>

  <svg class="card card--back" viewBox="0 0 795 454" role="group" aria-label="Card back">
    <text class="condensed watermark" x="450" y="470" font-size="180" textLength="380" lengthAdjust="spacingAndGlyphs" aria-hidden="true">fortyone</text>
    <text class="condensed wordmark" x="28" y="118" font-size="132" textLength="220" lengthAdjust="spacingAndGlyphs">fortyone</text>

    <line class="name-rule" x1="0" y1="209" x2="167" y2="209"/>
    <line class="name-rule" x1="633" y1="209" x2="795" y2="209"/>
    <text class="person-name" x="178" y="229" font-size="50" textLength="440" lengthAdjust="spacingAndGlyphs">MARCUS LEOW</text>
    <text class="condensed detail" x="276" y="265" font-size="30" textLength="241" lengthAdjust="spacingAndGlyphs">PRINCIPLE CONSULTANT</text>
    <text class="condensed detail" x="315" y="293" font-size="20" textLength="162" lengthAdjust="spacingAndGlyphs">F&amp;B AND HOSPITALITY</text>

    <g class="contact contact--phone">
      <circle class="icon-disc" cx="68" cy="354" r="25"/>
      <path class="icon-ink" d="M60 342c2-1 3 0 4 2l2 4c1 2 0 3-1 4-1 1 0 3 2 6s4 4 5 3c1-1 2-2 4-1l4 2c2 1 3 2 2 4-2 3-5 4-8 3-4-1-9-6-12-11s-5-11-2-16z"/>
      <text class="condensed detail" x="103" y="366" font-size="30" textLength="125" lengthAdjust="spacingAndGlyphs">(+65) 8364 5170</text>
    </g>
    <g class="contact contact--email">
      <circle class="icon-disc" cx="68" cy="416" r="25"/>
      <rect class="icon-line" x="55" y="407" width="26" height="18"/>
      <path class="icon-line" d="M55 407l13 11 13-11M55 425l10-9M81 425l-10-9"/>
      <text class="condensed detail" x="106" y="426" font-size="28" textLength="230" lengthAdjust="spacingAndGlyphs">marcus@fortyone-example.com.sg</text>
    </g>
  </svg>
</div>
</body>
</html>
```